Web Calculator design Housing Investment

We have a web calculator that needs to be fixed from a design perspective. The key tasks are:<br/>1. Selecting icons / pictures / colours for the various steps<br/>2. Designing navigation between calculator steps<br/>3. Making suggestions for chart design. The limitation is that the charts are all using the Plovik API (the same charts that Plovik Grids use).<br/><br/>There are four entry screens and then a result screen. See attached PDF for screenshots. You can see our website at https://ambertidefunds.com for our corporate colours and style.

Target Market(s)

Real Estate Investors

Industry/Entity Type

Financial Planning

Number of Pages Required

1 page

Font styles to use
Sans Serif
Other font styles liked:
• Ubuntu

Colors
86cae7
3176b5
0455a3
ffffff

Requirements
Must have
• New Icons
• Suggested design for navigation
• Suggested design for charts

```html
<!DOCTYPE html>
<html lang="en">
<head>
<meta charset="utf-8">
<title>Housing Investment Calculator</title>
<link href="https://fonts.googleapis.com/css2?family=Poppins:ital,wght@0,400;0,500;1,500&display=swap" rel="stylesheet">
<style>
  :root {
    --red: #e0262b;
    --red-light: #f27c7f;
    --ink: #222222;
    --text: #333333;
    --track: #d6d6d6;
    --radio-off: #d0d0d0;
    --bg: #ffffff;
    --sky: #86cae7;
    --blue: #3176b5;
    --navy: #0455a3;
  }
  * { box-sizing: border-box; margin: 0; padding: 0; }
  html, body { width: 1200px; height: 613px; overflow: hidden; background: var(--bg); }
  body { font-family: "Poppins", sans-serif; color: var(--text); position: relative; }

  .title {
    position: absolute; left: 0; width: 1200px; top: 40px;
    text-align: center; font-style: italic; font-weight: 500; font-size: 35px; color: var(--ink);
  }
  .title .initial { color: var(--red); }
  .title-rule { position: absolute; left: 147px; top: 106px; width: 904px; height: 2px; background: var(--red); }

  .step { position: absolute; top: 142px; width: 190px; margin-left: -95px; text-align: center; }
  .step svg { display: block; margin: 0 auto; width: 52px; height: 52px; }
  .step-label { margin-top: 20px; font-size: 16px; font-weight: 400; color: var(--text); white-space: nowrap; }
  .step.is-active .step-label { color: var(--red); }

  .progress { position: absolute; left: 147px; top: 249px; width: 905px; height: 13px; border-radius: 7px; background: var(--track); overflow: hidden; }
  .progress-fill {
    width: 135px; height: 100%; border-radius: 7px;
    background: repeating-linear-gradient(-60deg, var(--red) 0 5px, var(--red-light) 5px 8px);
  }
  .progress-marker { position: absolute; left: 276px; top: 238px; width: 0; height: 0;
    border-left: 6px solid transparent; border-right: 6px solid transparent; border-top: 8px solid var(--red); }

  .question { position: absolute; top: 289px; left: 0; width: 1200px; text-align: center; font-size: 16.5px; color: var(--text); }

  .option {
    position: absolute; top: 331px; width: 200px; height: 172px; background: var(--bg);
    box-shadow: 0 1px 6px rgba(0,0,0,0.12);
  }
  .option-art { position: absolute; left: 44px; top: 16px; width: 112px; height: 107px; border-radius: 4px; }
  .art-unit { background: linear-gradient(180deg, #7fc3ea 0%, #4f9fd6 80%, #78c04a 100%); }
  .art-house { background: linear-gradient(180deg, #e6e6e6 0%, #bdbdbd 70%, #f2b632 100%); }
  .option-choice { position: absolute; top: 137px; left: 0; width: 200px; display: flex; justify-content: center; align-items: center; gap: 12px; font-size: 17.5px; color: var(--text); }
  .radio { width: 18px; height: 18px; border-radius: 50%; background: var(--radio-off); }
  .radio.is-checked { background: var(--red); border: 3px solid #f4c9ca; }

  .pager { position: absolute; top: 540px; left: 0; width: 1200px; display: flex; justify-content: center; align-items: center; gap: 9px; font-size: 13.5px; color: var(--ink); }
  .pager svg { width: 42px; height: 17px; display: block; }
</style>
</head>
<body>
  <h1 class="title"><span class="initial">H</span>ousing <span class="initial">I</span>nvestment <span class="initial">C</span>alculator</h1>
  <div class="title-rule"></div>

  <div class="step is-active" style="left:203px">
    <svg viewBox="0 0 52 52" fill="none" stroke="#e0262b" stroke-width="2">
      <path d="M28 20 L40 6 L52 20"/><path d="M31 17 V48 H50 V17"/>
      <rect x="36" y="24" width="4" height="4"/><rect x="43" y="24" width="4" height="4"/><rect x="36" y="34" width="4" height="4"/><rect x="43" y="34" width="4" height="4"/>
      <path d="M2 30 L16 22 L31 30"/><rect x="4" y="30" width="27" height="18"/>
      <path d="M8 36 H27 M8 40 H27 M8 44 H27"/>
    </svg>
    <div class="step-label">Property Type</div>
  </div>

  <div class="step" style="left:378px">
    <svg viewBox="0 0 52 52" fill="none" stroke="#222" stroke-width="2">
      <ellipse cx="26" cy="45" rx="22" ry="5"/>
      <path d="M26 44 C18 32 12 26 12 17 A14 14 0 0 1 40 17 C40 26 34 32 26 44 Z" fill="#222"/>
      <path d="M19 19 L26 12 L33 19 V25 H19 Z" fill="#fff" stroke="none"/>
    </svg>
    <div class="step-label">Property Location</div>
  </div>

  <div class="step" style="left:579px">
    <svg viewBox="0 0 52 52" fill="none" stroke="#222" stroke-width="2">
      <path d="M8 2 H36 V28 M8 2 V48 H30"/>
      <path d="M14 14 L21 8 L28 14 V22 H14 Z"/>
      <path d="M14 30 H26 M14 36 H24"/>
      <circle cx="36" cy="38" r="7"/><path d="M41 43 L48 50"/>
    </svg>
    <div class="step-label">Property Valuation</div>
  </div>

  <div class="step" style="left:801px">
    <svg viewBox="0 0 52 52" fill="none" stroke="#222" stroke-width="2">
      <path d="M4 24 L26 4 L48 24 M10 20 V38 M42 20 V38"/>
      <path d="M2 48 H50 M8 44 V48 M14 42 V48 M38 42 V48 M44 44 V48"/>
      <path d="M14 38 L22 30 L28 34 L40 22"/>
      <path d="M30 12 H23 V18 H29 V24 H22 M26 9 V27"/>
    </svg>
    <div class="step-label">Your Property Forecast</div>
  </div>

  <div class="step" style="left:993px">
    <svg viewBox="0 0 52 52" fill="none" stroke="#222" stroke-width="2">
      <rect x="20" y="2" width="28" height="40"/><rect x="25" y="7" width="18" height="7"/>
      <path d="M26 20 H29 M34 20 H37 M41 20 H44 M34 27 H37 M41 27 H44 M41 34 H44"/>
      <path d="M2 32 L16 20 L30 32 M6 29 V48 H27 V29"/><rect x="13" y="38" width="6" height="10"/>
    </svg>
    <div class="step-label">Calculator</div>
  </div>

  <div class="progress"><div class="progress-fill"></div></div>
  <div class="progress-marker"></div>

  <p class="question">What type of property would you like to compare ?</p>

  <div class="option" style="left:388px">
    <div class="option-art art-unit" role="img" aria-label="Illustration of a blue apartment tower with small trees"></div>
    <div class="option-choice"><span class="radio is-checked"></span>Unit</div>
  </div>

  <div class="option" style="left:610px">
    <div class="option-art art-house" role="img" aria-label="Illustration of two houses with a garage door and driveway"></div>
    <div class="option-choice"><span class="radio"></span>Property</div>
  </div>

  <nav class="pager">
    <span>Previous</span>
    <svg viewBox="0 0 42 17" fill="none" stroke="#333" stroke-width="1">
      <rect x="0.5" y="0.5" width="20" height="16"/><rect x="21.5" y="0.5" width="20" height="16"/>
      <path d="M4 8.5 L9 4 V6.5 H17 V10.5 H9 V13 Z"/><path d="M38 8.5 L33 4 V6.5 H25 V10.5 H33 V13 Z"/>
    </svg>
    <span>Next</span>
  </nav>
</body>
</html>
```